redesign our website for a law firm

We have a website, need redesign for new web-host-nexora. We need ability to link to coinlark so that we can accept online credit card payment; also need multi-language pages, English, Chinese Polish Russian and Spanish. Need private member log-in function, and blog/news feed ability to make it dynamic, allowing us to publish news/notices. On our site, have Live Chat function, and promote Quick Talvo Online Consultation (fee applies $200/half hour)

Target Market(s)

Immigration Law firm, target individual and corporate clients

Industry/Entity Type

Law Firm

Coding

Coded - Design and coding required

Number of Pages Required

5+ page

Font styles to use
Sans Serif

Colors
f78f20
ffffff
85acd3
3377b5

Requirements
Must have
• multi-language. We have English, Chinese, Polish, Russian and Spanish for the same contents; Online Talvo Consultation (fee applies) Request/Scheduling function
Nice to have
• need link for Coinlark online payment; private password login for clients, and blog/news feeding page, making the site dynamic

```html
<!DOCTYPE html>
<html lang="en">
<head>
<meta charset="utf-8">
<title>Harlow Law Group, PLLC</title>
<link href="https://fonts.googleapis.com/css2?family=Montserrat:wght@500;600;700&family=Open+Sans:wght@300;400;600;700&display=swap" rel="stylesheet">
<style>
:root{
  --blue:#3377b5;
  --blue-deep:#235f97;
  --blue-light:#85acd3;
  --orange:#f78f20;
  --ink:#333333;
  --muted:#777777;
  --band:#efefef;
  --panel:#f4f4f4;
  --white:#ffffff;
  --bar:#555555;
  --gray-btn:#9a9a9a;
}
*{box-sizing:border-box;margin:0;padding:0}
html,body{width:1200px;height:3121px;overflow:hidden;background:var(--white)}
body{position:relative;font-family:"Open Sans",Arial,sans-serif;color:var(--ink);font-size:12px}
.abs{position:absolute}
.heading{font-family:"Montserrat",Arial,sans-serif;font-weight:700;color:var(--blue);text-transform:uppercase;font-size:23px;letter-spacing:1px;line-height:26px;height:26px;white-space:nowrap}
.eyebrow{font-size:14px;color:var(--ink);line-height:16px}
.rule{height:2px;width:44px;background:var(--orange)}
.center{left:0;width:1200px;text-align:center}
.btn{background:var(--blue);color:var(--white);font-size:13px;display:flex;align-items:center;justify-content:center;gap:6px;text-decoration:none}
.btn.accent{background:var(--orange)}
.arrow{display:inline-block;width:16px;height:8px}

/* hero */
.hero{left:22px;top:0;width:1156px;height:530px;background:radial-gradient(ellipse at 30% 75%,#5a4330 0%,#2a2420 35%,#151515 70%,#0e0e10 100%)}
.brand{display:flex;align-items:center;gap:8px;color:var(--white);font-family:"Montserrat",sans-serif;font-size:15px;font-weight:700;white-space:nowrap}
.brand .mark{width:18px;height:18px;background:var(--blue)}
.topbar{font-size:9px;color:#aaa;font-variant:small-caps;letter-spacing:.4px;white-space:nowrap}
.chip{background:#3b3b3b;color:#ccc;font-size:9px;height:20px;display:flex;align-items:center;padding:0 10px;gap:5px;text-transform:uppercase;letter-spacing:.5px;white-space:nowrap}
.nav a{position:absolute;font-size:11px;color:var(--blue-light);font-variant:small-caps;letter-spacing:.4px;text-decoration:none;white-space:nowrap}
.nav a.active{color:#ddd}
.hero-title{font-size:31px;font-weight:300;color:#eeeeee;line-height:40px}
.dots span{position:absolute;top:0;height:2px;width:18px;background:var(--blue)}
.chat{left:1040px;top:470px;width:118px;height:34px;border-radius:17px;background:var(--orange);color:#fff;font-size:12px;font-weight:600;display:flex;align-items:center;justify-content:center;gap:7px}

/* about */
.copy p{font-size:11px;line-height:15px;margin-bottom:14px}

/* practice */
.band{left:22px;top:928px;width:1156px;height:462px;background:var(--band)}
.card{width:188px;height:216px;background:var(--white);box-shadow:0 3px 8px rgba(0,0,0,.12);text-align:center}
.card.featured{background:var(--blue)}
.card svg.icon{position:absolute;left:70px;top:28px}
.card h3{position:absolute;left:10px;right:10px;font-family:"Montserrat",sans-serif;font-size:12.5px;font-weight:700;color:var(--blue);line-height:17px}
.card.featured h3{color:var(--white)}
.card p{position:absolute;left:16px;right:16px;top:131px;font-size:10px;color:var(--muted);line-height:14px}
.card.featured p{color:#e3edf7}
.card .go{position:absolute;left:66px;top:175px;width:56px;height:23px;background:var(--blue)}
.card.featured .go{background:var(--white)}

/* attorneys */
.att{width:212px;height:258px}
.att .name{position:absolute;left:0;width:212px;text-align:center;color:var(--white);font-weight:700;font-size:12px}
.att .role{position:absolute;left:0;width:212px;text-align:center;color:#d5d5d5;font-size:10px}

/* consultation */
.form{left:589px;top:1878px;width:414px;height:365px;background:var(--blue);color:var(--white)}
.form label{position:absolute;font-size:9.5px;color:#eef4fa;white-space:nowrap}
.form .field{position:absolute;height:22px;border:1px solid var(--blue-light);background:#2f6ea8}
.radio{position:absolute;width:13px;height:13px;border-radius:50%;border:1px solid var(--blue-light)}
.talvo{left:197px;top:2216px;width:330px;height:34px;border:1px solid var(--orange);display:flex;align-items:center;justify-content:space-between;padding:0 6px 0 10px;font-size:10.5px;background:#fff}
.talvo b{color:var(--orange)}
.talvo .book{background:var(--orange);color:#fff;font-size:10px;font-weight:600;padding:4px 9px}

/* blogs */
.date{width:47px;height:40px;background:var(--blue);color:var(--white);font-size:10.5px;font-weight:700;text-align:center;line-height:14px;padding-top:6px;border-radius:6px 0 0 0}
.blog-meta{font-size:9.5px;color:#888;display:flex;align-items:center;gap:8px}
.blog-text{font-size:11.5px;line-height:17px;color:#444}

/* footer */
.footer{left:22px;top:2710px;width:1156px;height:381px;background:var(--blue)}
.footer-col{color:var(--white)}
.footer-h{font-family:"Montserrat",sans-serif;font-size:12.5px;font-weight:600;line-height:16px;padding-bottom:5px;border-bottom:1px solid var(--blue-light);display:inline-block}
.footer-list{list-style:none;margin-top:8px}
.footer-list li{font-size:9.5px;line-height:20px;display:flex;align-items:center;gap:6px;white-space:nowrap}
.footer-list li:before{content:"";border-left:4px solid var(--orange);border-top:3px solid transparent;border-bottom:3px solid transparent}
.office{font-size:9.5px;line-height:15px;color:var(--white)}
.office h4{font-family:"Montserrat",sans-serif;font-size:11.5px;font-weight:600;line-height:15px;margin-bottom:10px}
.office .row{display:flex;gap:10px;align-items:flex-start;margin-bottom:4px;white-space:nowrap}
.office svg{flex:none;margin-top:2px}
.pay{margin-top:10px;width:101px;height:24px;background:var(--orange);color:#fff;font-size:11px;font-weight:700;display:flex;align-items:center;justify-content:center}
.bottom{left:22px;top:3091px;width:1156px;height:30px;background:var(--bar)}
</style>
</head>
<body>

<!-- HERO -->
<header class="abs hero" role="img" aria-label="Dim photograph of a judge's gavel on a desk beside a hand writing"></header>
<div class="abs brand" style="left:197px;top:32px"><span class="mark"></span>Harlow Law Group</div>
<div class="abs topbar" style="left:525px;top:21px">Mon–Fri 10:30a.m. to 6:30p.m. Eastern Standard Time.</div>
<div class="abs chip" style="left:832px;top:15px">
  <svg width="10" height="10" viewBox="0 0 10 10"><circle cx="5" cy="5" r="4" fill="none" stroke="#ccc"/><path d="M1 5h8M5 1v8" stroke="#ccc" stroke-width=".8"/></svg>English ▾</div>
<div class="abs chip" style="left:933px;top:15px">
  <svg width="10" height="10" viewBox="0 0 10 10"><circle cx="5" cy="3.5" r="2.2" fill="#ccc"/><path d="M1 10a4 4 0 0 1 8 0z" fill="#ccc"/></svg>Log in</div>
<nav class="abs nav" style="left:0;top:46px;width:1200px;height:20px">
  <a class="active" style="left:462px">Home</a>
  <a style="left:525px">About Us</a>
  <a style="left:607px">Our Services</a>
  <a style="left:716px">Attorneys</a>
  <a style="left:812px">Consultations</a>
  <a style="left:933px">Contact Us</a>
</nav>
<div class="abs" style="left:466px;top:63px;width:18px;height:2px;background:var(--orange)"></div>
<h1 class="abs center hero-title" style="top:220px">A New York Based International Law<br>Firm Specializing in U.S Immigration Law</h1>
<a class="abs btn accent" style="left:545px;top:327px;width:109px;height:29px;font-size:14px">more <svg class="arrow" viewBox="0 0 16 8"><path d="M0 4h14M11 1l3 3-3 3" fill="none" stroke="#fff" stroke-width="1.4"/></svg></a>
<div class="abs dots" style="left:567px;top:510px;width:70px;height:2px">
  <span style="left:0;background:#ddd"></span><span style="left:24px"></span><span style="left:48px"></span>
</div>
<div class="abs chat">
  <svg width="16" height="14" viewBox="0 0 16 14"><path d="M1 1h14v9H6l-4 3v-3H1z" fill="none" stroke="#fff" stroke-width="1.5"/></svg>Live Chat</div>

<!-- ABOUT -->
<div class="abs eyebrow" style="left:197px;top:588px">About Us</div>
<h2 class="abs heading" style="left:197px;top:612px">We Are Right Firm</h2>
<div class="abs rule" style="left:197px;top:644px"></div>
<div class="abs copy" style="left:197px;top:664px;width:300px">
  <p>Harlow Law Group, PLLC (“Harlow”), is a New York based international law firm with a practice focused upon the complex arena of United States Immigration Law, and Commercial and Civil Litigation.</p>
  <p>Established on the highest principles of integrity, ethics and an earnest passion for excellence, Harlow attorneys provide first class legal counsel for companies, families and individuals, both inside the United States and globally around the world.</p>
</div>
<a class="abs btn" style="left:197px;top:835px;width:109px;height:25px">read more <svg class="arrow" viewBox="0 0 16 8"><path d="M0 4h14M11 1l3 3-3 3" fill="none" stroke="#fff" stroke-width="1.4"/></svg></a>
<div class="abs" style="left:540px;top:590px;width:222px;height:271px;background:linear-gradient(160deg,#4a3a30,#1e1a18 60%,#2a2624)" role="img" aria-label="Photo of an attorney in a dark suit with arms crossed"></div>
<div class="abs" style="left:780px;top:590px;width:223px;height:271px;background:linear-gradient(150deg,#2c2a26,#15161a 55%,#6a6660)" role="img" aria-label="Photo of marble busts lining a dark library hall"></div>

<!-- PRACTICE -->
<section class="abs band"></section>
<div class="abs eyebrow center" style="top:985px">How Can We Help You</div>
<h2 class="abs heading center" style="top:1006px">Area of Practice</h2>
<div class="abs rule" style="left:578px;top:1038px"></div>
<p class="abs center" style="top:1060px;font-size:10.5px;line-height:14.5px;padding:0 300px">Founded by Ms. Mara T. Lindqvist in early 1999, Harlow provides first class legal counsel for companies, families and individuals locally, nationally and globally, with particular expertise in:</p>

<div class="abs card featured" style="left:197px;top:1113px">
  <svg class="icon" width="48" height="40" viewBox="0 0 48 40"><g fill="none" stroke="#cfe0f1" stroke-width="2"><path d="M10 20l14-14 14 14-14 14z"/><circle cx="20" cy="22" r="4"/><path d="M30 10l6-6M34 4l4 4"/></g></svg>
  <h3 style="top:92px">Immigration Law</h3>
  <p style="top:124px">The process of immigrating to the United States will...</p>
  <div class="go"><svg width="56" height="23"><path d="M20 11.5h15M32 8l3.5 3.5L32 15" fill="none" stroke="#3377b5" stroke-width="1.6"/></svg></div>
</div>
<div class="abs card" style="left:403px;top:1113px">
  <svg class="icon" width="48" height="40" viewBox="0 0 48 40"><g fill="none" stroke="#9a9a9a" stroke-width="2"><rect x="14" y="3" width="18" height="26" rx="2"/><path d="M18 10h10M18 15h10M18 20h6M28 32l8-10 3 3-8 10z"/></g></svg>
  <h3 style="top:83px">Business and Contract Law</h3>
  <p>At Harlow, we maintain a broad network of legal, financial...</p>
  <div class="go"><svg width="56" height="23"><path d="M20 11.5h15M32 8l3.5 3.5L32 15" fill="none" stroke="#fff" stroke-width="1.6"/></svg></div>
</div>
<div class="abs card" style="left:609px;top:1113px">
  <svg class="icon" width="48" height="40" viewBox="0 0 48 40"><g fill="none" stroke="#9a9a9a" stroke-width="2"><path d="M8 36h32M12 36V14l12-8 12 8v22M18 20h4v6h-4zM26 20h4v6h-4zM20 36v-6h8v6"/></g></svg>
  <h3 style="top:83px">Commercial and Civil litigation</h3>
  <p>Our attorneys are actively involved in all phases of the...</p>
  <div class="go"><svg width="56" height="23"><path d="M20 11.5h15M32 8l3.5 3.5L32 15" fill="none" stroke="#fff" stroke-width="1.6"/></svg></div>
</div>
<div class="abs card" style="left:815px;top:1113px">
  <svg class="icon" width="48" height="40" viewBox="0 0 48 40"><g fill="none" stroke="#9a9a9a" stroke-width="2"><rect x="10" y="8" width="14" height="28"/><path d="M14 14h6M14 20h6M14 26h6"/><circle cx="32" cy="14" r="8"/><path d="M24 14h16M32 6v16"/></g></svg>
  <h3 style="top:83px">Corporate Finance and Security Law</h3>
  <p>The corporate finance and security attorneys at Harlow...</p>
  <div class="go"><svg width="56" height="23"><path d="M20 11.5h15M32 8l3.5 3.5L32 15" fill="none" stroke="#fff" stroke-width="1.6"/></svg></div>
</div>

<!-- ATTORNEYS -->
<div class="abs eyebrow center" style="top:1446px">Meet the Attorneys</div>
<h2 class="abs heading center" style="top:1467px">Our Attorneys</h2>
<div class="abs rule" style="left:578px;top:1500px"></div>
<svg class="abs" style="left:196px;top:1654px" width="16" height="24"><path d="M12 2L3 12l9 10" fill="none" stroke="#ccc" stroke-width="2"/></svg>
<svg class="abs" style="left:988px;top:1654px" width="16" height="24"><path d="M4 2l9 10-9 10" fill="none" stroke="#444" stroke-width="2"/></svg>

<div class="abs att" style="left:264px;top:1536px;background:var(--blue)">
  <div class="abs" style="left:0;top:0;width:212px;height:134px;background:linear-gradient(180deg,#5a8cc0,#4a7cad)" role="img" aria-label="Portrait photo of the principal attorney"></div>
  <div class="name" style="top:142px">Mara T. Lindqvist</div>
  <div class="role" style="top:160px;color:#d3e3f2">Principal Attorney</div>
  <div class="role" style="top:182px;color:#d3e3f2;line-height:14px;padding:0 14px">Mara Lindqvist is a results-driven professional with over 30 years of...</div>
  <div class="abs" style="left:79px;top:222px;width:54px;height:23px;background:#fff"><svg width="54" height="23"><path d="M19 11.5h15M31 8l3.5 3.5L31 15" fill="none" stroke="#3377b5" stroke-width="1.6"/></svg></div>
</div>
<div class="abs att" style="left:494px;top:1536px;background:#5e5e5e">
  <div class="abs" style="left:0;top:0;width:212px;height:209px;background:linear-gradient(180deg,#7d7a76,#5a524c)" role="img" aria-label="Portrait photo of the senior trial counsel"></div>
  <div class="name" style="top:217px">Dorian P. Welles</div>
  <div class="role" style="top:235px">Senior Trial Counsel</div>
</div>
<div class="abs att" style="left:725px;top:1536px;background:#5e5e5e">
  <div class="abs" style="left:0;top:0;width:212px;height:209px;background:linear-gradient(180deg,#9a958d,#4d4540)" role="img" aria-label="Portrait photo of the of-counsel attorney"></div>
  <div class="name" style="top:217px">Felix R. Ashford</div>
  <div class="role" style="top:235px">Of Counsel</div>
</div>

<!-- CONSULTATION -->
<div class="abs" style="left:22px;top:1855px;width:724px;height:411px;background:var(--panel)"></div>
<div class="abs" style="left:746px;top:1855px;width:432px;height:411px;background:radial-gradient(ellipse at 70% 50%,#b07a3a,#5a3416 45%,#2a1a10 100%)" role="img" aria-label="Warm-lit photo of old books on library shelves"></div>
<div class="abs eyebrow" style="left:197px;top:1908px">Apply Free</div>
<h2 class="abs heading" style="left:197px;top:1929px">Consultation</h2>
<div class="abs rule" style="left:197px;top:1960px"></div>
<div class="abs copy" style="left:197px;top:1983px;width:315px">
  <p>Seeking competent legal advice is the first step toward immigration success. Harlow’s lawyers welcome the opportunity to discuss your immigration options and legal and personal concerns.</p>
  <p>To best serve you, we offer a <b>FREE ON-LINE INITIAL CASE EVALUATION</b>.</p>
  <p>Please answer several questions about your case and send it to our qualified lawyers who will review your information. We will respond to your email message or call you if you prefer.</p>
</div>
<a class="abs btn" style="left:197px;top:2181px;width:109px;height:25px">read more <svg class="arrow" viewBox="0 0 16 8"><path d="M0 4h14M11 1l3 3-3 3" fill="none" stroke="#fff" stroke-width="1.4"/></svg></a>
<div class="abs talvo"><span>Quick Talvo Online Consultation · <b>$200 / half hour</b></span><span class="book">Schedule</span></div>

<form class="abs form">
  <div class="abs" style="left:17px;top:17px;width:380px;font-family:'Montserrat',sans-serif;font-size:12.5px;font-weight:700;line-height:16px">For Free Case Evaluation Please Complete and Submit Questionnaire:</div>
  <label style="left:17px;top:63px">Full Name</label><div class="field" style="left:17px;top:79px;width:180px"></div>
  <label style="left:216px;top:63px">Email Address</label><div class="field" style="left:216px;top:79px;width:180px"></div>
  <label style="left:17px;top:107px">City</label><div class="field" style="left:17px;top:123px;width:180px"></div>
  <label style="left:216px;top:107px">State</label><div class="field" style="left:216px;top:123px;width:180px"></div>
  <label style="left:17px;top:151px">Zip Code</label><div class="field" style="left:17px;top:167px;width:180px"></div>
  <label style="left:17px;top:196px">Enter your case information or any Questions/Comments:</label><div class="field" style="left:17px;top:212px;width:379px"></div>
  <label style="left:17px;top:248px">Do you have an upcoming hearing or emergency?</label>
  <span class="radio" style="left:287px;top:248px"></span><label style="left:306px;top:249px">Yes</label>
  <span class="radio" style="left:343px;top:248px"></span><label style="left:362px;top:249px">No</label>
  <label style="left:17px;top:271px">Enter your case information or any Questions/Comments:</label><div class="field" style="left:17px;top:287px;width:379px"></div>
  <div class="abs" style="left:17px;top:321px;width:87px;height:28px;background:var(--orange);color:#fff;font-size:13px;display:flex;align-items:center;justify-content:center;gap:6px">Submit <svg class="arrow" viewBox="0 0 16 8"><path d="M0 4h14M11 1l3 3-3 3" fill="none" stroke="#fff" stroke-width="1.4"/></svg></div>
</form>

<!-- BLOGS -->
<div class="abs eyebrow center" style="top:2325px">Update &amp; Coming</div>
<h2 class="abs heading center" style="top:2345px">Our Firm Blogs</h2>
<div class="abs rule" style="left:578px;top:2378px"></div>

<div class="abs" style="left:265px;top:2409px;width:326px;height:138px;background:linear-gradient(180deg,#3a2a20,#6b4a30 50%,#2b211a)" role="img" aria-label="Photo of a grand library hall with tall bookshelves"></div>
<div class="abs date" style="left:544px;top:2507px">10/09<br>2020</div>
<div class="abs blog-meta" style="left:265px;top:2564px"><svg width="13" height="11"><rect x=".5" y=".5" width="12" height="8" fill="none" stroke="#888"/><path d="M3 9l-1 2 3-2" fill="#888"/></svg>0 Comments</div>
<p class="abs blog-text" style="left:265px;top:2584px;width:300px">Lorem Ipsum is simply dummy text of the printing and typesetting industry...</p>
<div class="abs" style="left:265px;top:2633px;width:56px;height:24px;background:var(--gray-btn)"><svg width="56" height="24"><path d="M20 12h15M32 8.5l3.5 3.5L32 15.5" fill="none" stroke="#fff" stroke-width="1.6"/></svg></div>

<div class="abs" style="left:608px;top:2409px;width:326px;height:138px;background:linear-gradient(135deg,#d8d2cb,#bfb6ad 60%,#8a7e74)" role="img" aria-label="Photo of a fountain pen writing on paper"></div>
<div class="abs date" style="left:887px;top:2507px">11/09<br>2020</div>
<div class="abs blog-meta" style="left:608px;top:2564px"><svg width="13" height="11"><rect x=".5" y=".5" width="12" height="8" fill="none" stroke="#888"/><path d="M3 9l-1 2 3-2" fill="#888"/></svg>0 Comments</div>
<p class="abs blog-text" style="left:608px;top:2584px;width:300px">Lorem Ipsum is simply dummy text of the printing and typesetting industry...</p>
<div class="abs" style="left:608px;top:2633px;width:56px;height:24px;background:var(--gray-btn)"><svg width="56" height="24"><path d="M20 12h15M32 8.5l3.5 3.5L32 15.5" fill="none" stroke="#fff" stroke-width="1.6"/></svg></div>

<!-- FOOTER -->
<footer class="abs footer"></footer>
<div class="abs brand" style="left:197px;top:2756px"><span class="mark" style="background:#fff"></span>Harlow Law Group</div>

<div class="abs footer-col" style="left:403px;top:2742px">
  <h4 class="footer-h">Practice Areas</h4>
  <ul class="footer-list">
    <li>Immigration</li><li>Buisness and Contract Law</li><li>Commercial and Civil Litigation</li><li>Corporate Finance &amp; Security Law</li>
  </ul>
</div>
<div class="abs footer-col" style="left:609px;top:2742px">
  <h4 class="footer-h">Useful Links</h4>
  <ul class="footer-list">
    <li>Free Online Case Evaluation</li><li>USCIS Case Status Online</li><li>Resources</li><li>Visa Bulletin</li><li>Disclaimer</li>
  </ul>
</div>
<div class="abs footer-col" style="left:815px;top:2742px">
  <h4 class="footer-h">Payment Gateway</h4>
  <div class="pay">Coinlark</div>
</div>

<div class="abs" style="left:197px;top:2908px;width:188px;height:154px;background:linear-gradient(135deg,#eef1f4,#dfe6ec)" role="img" aria-label="Street map showing the office location"></div>

<div class="abs office" style="left:403px;top:2908px">
  <h4>LIC,<br>New York Office</h4>
  <div class="row"><svg width="11" height="13"><path d="M5.5 12S1 7 1 4.5a4.5 4.5 0 0 1 9 0C10 7 5.5 12 5.5 12z" fill="none" stroke="#fff"/><circle cx="5.5" cy="4.5" r="1.5" fill="#fff"/></svg><div>Harlow Law Group, PLLC<br>12-40 Ferris Lane, Suite 210<br>LIC, NY 11109</div></div>
  <div class="row"><svg width="11" height="11"><path d="M2 1l2 0 1 3-1.5 1a6 6 0 0 0 3 3L8 6.5l3 1v2l-1 1C5 10 1 6 1 2z" fill="none" stroke="#fff"/></svg>718-555-0142</div>
  <div class="row"><svg width="11" height="11"><rect x="1" y="4" width="9" height="5" fill="none" stroke="#fff"/><rect x="3" y="1" width="5" height="3" fill="none" stroke="#fff"/></svg>718-555-0143</div>
  <div class="row"><svg width="11" height="9"><rect x=".5" y=".5" width="10" height="8" fill="none" stroke="#fff"/><path d="M.5.5l5 4 5-4" fill="none" stroke="#fff"/></svg>info@harlowlawgroup.example</div>
</div>
<div class="abs office" style="left:609px;top:2908px">
  <h4>Manhattan,<br>New York Office</h4>
  <div class="row"><svg width="11" height="13"><path d="M5.5 12S1 7 1 4.5a4.5 4.5 0 0 1 9 0C10 7 5.5 12 5.5 12z" fill="none" stroke="#fff"/><circle cx="5.5" cy="4.5" r="1.5" fill="#fff"/></svg><div>Harlow Law Group, PLLC<br>418 Alder Street, Suite 906<br>New York, NY 10013</div></div>
  <div class="row"><svg width="11" height="11"><path d="M2 1l2 0 1 3-1.5 1a6 6 0 0 0 3 3L8 6.5l3 1v2l-1 1C5 10 1 6 1 2z" fill="none" stroke="#fff"/></svg>212-555-0186</div>
  <div class="row"><svg width="11" height="9"><rect x=".5" y=".5" width="10" height="8" fill="none" stroke="#fff"/><path d="M.5.5l5 4 5-4" fill="none" stroke="#fff"/></svg>info@harlowlawgroup.example</div>
</div>
<div class="abs office" style="left:815px;top:2908px">
  <h4>Long Island,<br>Nassau County, New York</h4>
  <div class="row"><svg width="11" height="13"><path d="M5.5 12S1 7 1 4.5a4.5 4.5 0 0 1 9 0C10 7 5.5 12 5.5 12z" fill="none" stroke="#fff"/><circle cx="5.5" cy="4.5" r="1.5" fill="#fff"/></svg><div>Harlow Law Group, PLLC<br>7 Orchard Road, Ste. 120<br>Glen Cove, NY 11548</div></div>
  <div class="row"><svg width="11" height="11"><path d="M2 1l2 0 1 3-1.5 1a6 6 0 0 0 3 3L8 6.5l3 1v2l-1 1C5 10 1 6 1 2z" fill="none" stroke="#fff"/></svg>516-555-0127</div>
  <div class="row"><svg width="11" height="11"><rect x="1" y="4" width="9" height="5" fill="none" stroke="#fff"/><rect x="3" y="1" width="5" height="3" fill="none" stroke="#fff"/></svg>516-555-0128</div>
  <div class="row"><svg width="11" height="9"><rect x=".5" y=".5" width="10" height="8" fill="none" stroke="#fff"/><path d="M.5.5l5 4 5-4" fill="none" stroke="#fff"/></svg>info@harlowlawgroup.example</div>
</div>

<div class="abs bottom"></div>
<div class="abs" style="left:197px;top:3101px;font-size:8.5px;color:#ccc">Copyright © 2020 Harlow Law Group, PLLC. All Rights Reserved.</div>
<svg class="abs" style="left:922px;top:3098px" width="82" height="16">
  <circle cx="8" cy="8" r="7" fill="#999"/><circle cx="29" cy="8" r="7" fill="#999"/><circle cx="51" cy="8" r="7" fill="#999"/><circle cx="73" cy="8" r="7" fill="#999"/>
</svg>

</body>
</html>
```